The design should be a multi-page, foldable flyer with the logo and the product name on the front and the web address on the back.
DoLMUO is a word play on "zebra", which the design should reflect in some way.

Target Market(s)

Schools and individual teachers

Industry/Entity Type

Product

Colors
ffffff
000000

```html
<!DOCTYPE html>
<html lang="en">
<head>
<meta charset="utf-8">
<title>DoLMUO Folded Flyer</title>
<link href="https://fonts.googleapis.com/css2?family=Roboto+Condensed:wght@300;400;700&display=swap" rel="stylesheet">
<style>
  :root{
    --paper:#ffffff;
    --ink:#000000;
    --text:#2b2b2b;
    --logo-grey:#4a4a4a;
    --stripe-light:#f3f3f3;
    --stripe-mid:#d9d9d9;
    --stage:#ececec;
    --create:#8dba2c;
    --revise:#e39a2c;
    --analyze:#2a9fb0;
    --perform:#c8392a;
    --administrate:#3c76c0;
  }
  *{box-sizing:border-box;margin:0;padding:0}
  html,body{width:802px;height:1200px;overflow:hidden}
  body{background:var(--stage);font-family:"Roboto Condensed",Arial,sans-serif;color:var(--text);position:relative}

  .page{position:absolute;background:var(--paper);box-shadow:0 4px 14px rgba(0,0,0,.18);overflow:hidden}
  .page svg.page-art{position:absolute;inset:0}

  /* covers */
  .cover-front{left:130px;top:20px;width:250px;height:560px}
  .cover-back{left:422px;top:20px;width:250px;height:560px}

  .brand{position:absolute;display:flex;align-items:center;gap:8px}
  .brand-dot{width:22px;height:22px;border-radius:50%;background:var(--logo-grey);flex:none}
  .brand-name{font-weight:300;font-size:36px;color:var(--logo-grey);letter-spacing:1px;line-height:1;white-space:nowrap}
  .cover-front .brand{left:28px;top:280px}
  .brand-tagline{position:absolute;left:28px;top:324px;font-size:8.5px;color:var(--logo-grey);white-space:nowrap}
  .cover-back .brand{left:52px;top:264px}
  .web-address{position:absolute;right:22px;bottom:40px;font-weight:700;font-size:15px;color:var(--ink);white-space:nowrap}

  /* inside spread */
  .spread{position:absolute;left:121px;top:610px;width:560px;height:570px;background:var(--paper);box-shadow:0 4px 14px rgba(0,0,0,.18);overflow:hidden}
  .spread-pattern{position:absolute;inset:0;background:
      linear-gradient(115deg,var(--stripe-light) 0%,var(--stripe-mid) 30%,var(--stripe-light) 55%,var(--stripe-mid) 80%,var(--stripe-light) 100%)}
  .fold{position:absolute;left:279px;top:0;width:2px;height:100%;background:linear-gradient(90deg,rgba(0,0,0,.08),rgba(0,0,0,0))}
  .inner-page{position:absolute;top:0;width:280px;height:570px}
  .inner-left{left:0}
  .inner-right{left:280px}

  .module{position:absolute}
  .module-head{position:relative;height:64px;width:240px}
  .module-head svg{position:absolute;left:0;top:0}
  .module-title{position:absolute;top:34px;font-weight:700;font-size:17px;letter-spacing:3.5px;color:var(--text);line-height:1;white-space:nowrap}
  .module-title.on-tag{color:var(--paper)}
  .module-text{font-size:9px;line-height:11.5px;color:var(--text);margin-top:8px}
  .module-text b{font-weight:700}

  .task-list{display:grid;grid-template-columns:122px 120px;row-gap:6px;list-style:none;margin-top:22px;padding-left:6px;font-size:9px}
  .task-list li{display:flex;align-items:center;gap:7px;white-space:nowrap}
  .task-list li::before{content:"";width:7px;height:7px;border-radius:50%;border:1.5px solid #666;flex:none}
</style>
</head>
<body>

<!-- front cover -->
<section class="page cover-front">
  <svg class="page-art" width="250" height="560" viewBox="0 0 250 560">
    <defs>
      <linearGradient id="photoTone" x1="0" y1="0" x2="1" y2="1">
        <stop offset="0" stop-color="#b9c4cc"/><stop offset=".6" stop-color="#8c7a6a"/><stop offset="1" stop-color="#5a4a40"/>
      </linearGradient>
      <linearGradient id="chartTone" x1="0" y1="0" x2="1" y2="1">
        <stop offset="0" stop-color="#d9e6f0"/><stop offset="1" stop-color="#9fc1db"/>
      </linearGradient>
    </defs>
    <polygon points="0,0 250,0 250,100 0,210" fill="url(#photoTone)" role="img" aria-label="Photo of students working at computers in a classroom"/>
    <polygon points="0,210 250,100 250,155 0,265" fill="var(--ink)"/>
    <polygon points="0,470 250,360 250,415 0,525" fill="var(--ink)"/>
    <rect x="75" y="470" width="105" height="75" rx="6" fill="url(#chartTone)" role="img" aria-label="Illustration of reports with bar and pie charts"/>
  </svg>
  <div class="brand"><span class="brand-dot"></span><span class="brand-name">DoLMUO</span></div>
  <p class="brand-tagline">Smart testing tools for every classroom</p>
</section>

<!-- back cover -->
<section class="page cover-back">
  <svg class="page-art" width="250" height="560" viewBox="0 0 250 560">
    <defs>
      <linearGradient id="zebraBack" x1="0" y1="0" x2="1" y2="1">
        <stop offset="0" stop-color="#e6e6e6"/><stop offset=".5" stop-color="#c9c9c9"/><stop offset="1" stop-color="#e0e0e0"/>
      </linearGradient>
    </defs>
    <rect width="250" height="560" fill="url(#zebraBack)" role="img" aria-label="Grey zebra stripe pattern"/>
    <polygon points="0,90 250,200 250,255 0,145" fill="var(--ink)"/>
    <polygon points="0,350 250,460 250,515 0,405" fill="var(--ink)"/>
  </svg>
  <div class="brand"><span class="brand-dot"></span><span class="brand-name">DoLMUO</span></div>
  <p class="web-address">www.dolmuo.com</p>
</section>

<!-- inside spread -->
<section class="spread">
  <div class="spread-pattern" role="img" aria-label="Light grey zebra stripe pattern"></div>
  <div class="fold"></div>

  <div class="inner-page inner-left">
    <article class="module" style="left:28px;top:26px;width:232px">
      <div class="module-head">
        <svg width="80" height="64"><polygon points="12,4 76,0 80,62 4,58" fill="#555" transform="translate(2,3)"/><polygon points="12,4 76,0 78,58 0,56" fill="var(--create)"/></svg>
        <span class="module-title" style="left:22px">CREATE</span>
        <span class="module-title on-tag" style="left:22px;clip-path:inset(0 calc(100% - 56px) 0 0)">CREATE</span>
      </div>
      <p class="module-text">The <b>CREATE-Module</b> lets you manage your Tasks and Tests easily by providing repositories in which they reside.<br>By continuously expanding the Task-Repository you can reduce the workload for each new Test you create by being able to reuse and adjust existing Tasks.<br>At the moment Tasks can contain the following elements:</p>
      <ul class="task-list">
        <li>Free Text</li><li>True-False-Justification</li>
        <li>Word-/Sentence Gap</li><li>Images</li>
        <li>Descriptions</li><li>Audio Files</li>
        <li>Math Containers</li><li>Sentence Matching</li>
        <li>Multiple Choice</li><li>Headings</li>
        <li>Short Answers</li>
      </ul>
    </article>

    <article class="module" style="left:28px;top:372px;width:232px">
      <div class="module-head">
        <svg width="86" height="64"><polygon points="8,8 82,0 84,62 2,58" fill="#555" transform="translate(2,3)"/><polygon points="8,8 82,0 82,58 0,56" fill="var(--perform)"/></svg>
        <span class="module-title" style="left:26px">PERFORM</span>
        <span class="module-title on-tag" style="left:26px;clip-path:inset(0 calc(100% - 56px) 0 0)">PERFORM</span>
      </div>
      <p class="module-text">The <b>PERFORM-Module</b> lets your students perform the tests you created. During sessions you are able to monitor what students are producing and you can also pause or stop tests for individual students – for example if you suspect that someone is cheating - or the entire class. The system also keeps track of where students are situated during tests, in order for you to be able reveal cheating attempts afterwards.</p>
    </article>
  </div>

  <div class="inner-page inner-right">
    <article class="module" style="left:22px;top:22px;width:250px">
      <div class="module-head">
        <svg width="84" height="64"><polygon points="14,0 80,4 76,62 0,58" fill="#555" transform="translate(2,3)"/><polygon points="14,0 80,4 74,58 0,56" fill="var(--revise)"/></svg>
        <span class="module-title" style="left:38px">REVISE</span>
        <span class="module-title on-tag" style="left:38px;clip-path:inset(0 calc(100% - 38px) 0 0)">REVISE</span>
      </div>
      <p class="module-text">With the <b>REVISE-Module</b> you can mark the tests previously performed by your students. A lot of different types of tasks can be auto-marked by the system – e.g. Multiple Choice, Short Answers, etc. – freeing you up to concentrate on marking textual work.<br>When marking texts, you can define your own custom error types, allowing you to personalize your markings and to give students the best possible feedback.</p>
    </article>

    <article class="module" style="left:22px;top:210px;width:250px">
      <div class="module-head">
        <svg width="92" height="64"><polygon points="16,0 88,4 84,62 0,58" fill="#555" transform="translate(2,3)"/><polygon points="16,0 88,4 82,58 0,56" fill="var(--analyze)"/></svg>
        <span class="module-title" style="left:24px">ANALYZE</span>
        <span class="module-title on-tag" style="left:24px;clip-path:inset(0 calc(100% - 60px) 0 0)">ANALYZE</span>
      </div>
      <p class="module-text">The <b>ANALYZE-Module</b> provides several different reports and tools that help you understand the data within your system, like how student performance has changed over time in general or how they perform on specific tasks, tests or even subjects</p>
    </article>

    <article class="module" style="left:22px;top:368px;width:250px">
      <div class="module-head">
        <svg width="84" height="64"><polygon points="14,0 80,4 76,62 0,58" fill="#555" transform="translate(2,3)"/><polygon points="14,0 80,4 74,58 0,56" fill="var(--administrate)"/></svg>
        <span class="module-title" style="left:24px">ADMINISTRATE</span>
        <span class="module-title on-tag" style="left:24px;clip-path:inset(0 calc(100% - 52px) 0 0)">ADMINISTRATE</span>
      </div>
      <p class="module-text">The <b>ADMINISTRATE-Module</b> contains all administrative data you need within the system. Here you can create, update and delete users, assign them different roles and rights that govern what they are and are not allowed to do and manage your subjects and classes.</p>
    </article>
  </div>
</section>

</body>
</html>
```